New Business Card Design*

We are a recruitment company based in Norwich/Cambridge England.
I have included our company logo which we want to remain the same.

What we are looking for is a new creative Business card which will really stand out!!

Contact Information for Business Card

Harriet Vance
email: Harriet@brelvix.co.uk
Address: Tolworth House
Ashgrove Innovation Park
Pelham Road
Norwich
KT9 3QD
Tel:01632 960418

```html
<!DOCTYPE html>
<html lang="en">
<head>
<meta charset="utf-8">
<title>Brelvix Business Card</title>
<link rel="stylesheet" href="https://fonts.googleapis.com/css2?family=Montserrat:wght@400;500;600&display=swap">
<style>
  :root {
    --backdrop: #eceee8;
    --card: #fcfcfa;
    --green: #8cc63f;
    --green-light: #a6d45a;
    --green-deep: #76b82a;
    --grey: #808285;
    --grey-dark: #636466;
    --grey-light: #b4b5b8;
    --grey-pale: #d3d4d6;
    --ink: #6d6e71;
    --white: #ffffff;
  }
  * { box-sizing: border-box; margin: 0; padding: 0; }
  html, body {
    width: 1200px;
    height: 1042px;
    overflow: hidden;
    background: var(--backdrop);
    font-family: "Montserrat", Arial, sans-serif;
  }
  .canvas {
    position: relative;
    width: 1200px;
    height: 1042px;
  }
  .card {
    position: absolute;
    left: 220px;
    width: 760px;
    height: 436px;
    background: var(--card);
    overflow: hidden;
    box-shadow: 0 14px 30px rgba(40, 60, 20, 0.22);
  }
  .card--front { top: 60px; }
  .card--back { top: 546px; }
  .card-art {
    position: absolute;
    inset: 0;
    width: 100%;
    height: 100%;
  }
  .brand {
    position: absolute;
    display: flex;
    align-items: center;
    gap: 14px;
  }
  .brand-dot {
    border-radius: 50%;
    background: var(--green);
  }
  .brand-name {
    color: var(--grey);
    font-weight: 600;
    letter-spacing: -0.5px;
  }
  .card--front .brand { left: 228px; top: 92px; }
  .card--front .brand-dot { width: 58px; height: 58px; }
  .card--front .brand-name { font-size: 58px; }

  .card--back .brand { left: 44px; top: 112px; }
  .card--back .brand-dot { width: 46px; height: 46px; }
  .card--back .brand-name { font-size: 46px; }

  .holder {
    position: absolute;
    right: 236px;
    top: 86px;
    text-align: right;
    color: var(--ink);
  }
  .holder-name {
    font-size: 17px;
    font-weight: 500;
    letter-spacing: 0.3px;
    text-transform: uppercase;
  }
  .holder-role {
    font-size: 11px;
    margin-top: 2px;
  }
  .address {
    position: absolute;
    left: 16px;
    top: 378px;
    font-size: 11.5px;
    font-weight: 500;
    color: var(--grey-dark);
    white-space: nowrap;
  }
  .contact {
    position: absolute;
    top: 410px;
    display: flex;
    align-items: center;
    gap: 10px;
    font-size: 12px;
    font-weight: 500;
    color: var(--white);
    white-space: nowrap;
  }
  .contact--phone { left: 30px; }
  .contact--email { left: 262px; }
  .contact-icon { width: 18px; height: 18px; }
</style>
</head>
<body>
<main class="canvas">

  <section class="card card--front" aria-label="Business card front">
    <svg class="card-art" viewBox="0 0 760 436" aria-hidden="true">
      <defs>
        <linearGradient id="frontGreen" x1="0" y1="1" x2="1" y2="0">
          <stop offset="0" stop-color="#7fbe35"/>
          <stop offset="1" stop-color="#a8d45c"/>
        </linearGradient>
      </defs>
      <polygon points="0,318 116,220 356,298 760,118 760,436 0,436" fill="#b9babd"/>
      <polygon points="0,334 124,236 360,313 760,138 760,436 0,436" fill="#737477"/>
      <polygon points="0,350 134,254 366,330 760,162 760,436 0,436" fill="url(#frontGreen)"/>
    </svg>
    <div class="brand">
      <span class="brand-dot"></span>
      <span class="brand-name">Brelvix</span>
    </div>
  </section>

  <section class="card card--back" aria-label="Business card back">
    <svg class="card-art" viewBox="0 0 760 436" aria-hidden="true">
      <defs>
        <linearGradient id="backGreen" x1="0" y1="0" x2="0" y2="1">
          <stop offset="0" stop-color="#98cc48"/>
          <stop offset="1" stop-color="#80bf38"/>
        </linearGradient>
        <linearGradient id="bandGrey" x1="0" y1="0" x2="1" y2="0">
          <stop offset="0" stop-color="#e6e7e8"/>
          <stop offset="1" stop-color="#a7a8ab"/>
        </linearGradient>
        <linearGradient id="bandDark" x1="0" y1="0" x2="1" y2="0">
          <stop offset="0" stop-color="#8a8b8e"/>
          <stop offset="1" stop-color="#5e5f62"/>
        </linearGradient>
      </defs>
      <polygon points="718,0 760,0 760,436 508,436 522,366 690,262" fill="#c3c4c6"/>
      <polygon points="728,0 760,0 760,436 520,436 533,366 699,264" fill="#6f7073"/>
      <polygon points="738,0 760,0 760,436 534,436 545,368 708,266" fill="url(#backGreen)"/>
      <polygon points="0,366 526,366 512,436 0,436" fill="url(#bandGrey)"/>
      <polygon points="0,402 519,402 512,436 0,436" fill="url(#bandDark)"/>
      <polygon points="0,362 527,362 526,368 0,368" fill="var(--green)"/>
    </svg>

    <div class="brand">
      <span class="brand-dot"></span>
      <span class="brand-name">Brelvix</span>
    </div>

    <div class="holder">
      <p class="holder-name">Harriet Vance</p>
      <p class="holder-role">Director</p>
    </div>

    <p class="address">Tolworth House Ashgrove Innovation Park Pelham Road Norwich KT9 3QD</p>

    <p class="contact contact--phone">
      <svg class="contact-icon" viewBox="0 0 24 24" aria-hidden="true">
        <path d="M6.6 10.8a15.1 15.1 0 0 0 6.6 6.6l2.2-2.2c.3-.3.7-.4 1-.2 1.1.4 2.3.6 3.6.6.6 0 1 .4 1 1V20c0 .6-.4 1-1 1C10.6 21 3 13.4 3 4c0-.6.4-1 1-1h3.5c.6 0 1 .4 1 1 0 1.3.2 2.5.6 3.6.1.3 0 .7-.2 1z" fill="#ffffff"/>
      </svg>
      01632 960418
    </p>
    <p class="contact contact--email">
      <svg class="contact-icon" viewBox="0 0 24 24" aria-hidden="true">
        <rect x="2.5" y="5" width="19" height="14" fill="none" stroke="#ffffff" stroke-width="1.6"/>
        <polyline points="2.5,5 12,13 21.5,5" fill="none" stroke="#ffffff" stroke-width="1.6"/>
      </svg>
      Harriet@brelvix.co.uk
    </p>
  </section>

</main>
</body>
</html>
```